Direct Mail Postcard- Lighting Company

Our task is to send a postcard directly to houses surrounding where our company has done work. My goal is to position ourselves as the go to outdoor lighting partner for their neighborhood.
Trusted Lighting Design & Maintenance Your neighbor chose us to enhance and maintain their home's beauty and security. Now, we're offering our top-tier services to the entire neighborhood.
Please emphasize our:
Maintenance Excellence:
Regular system check-ups
Prompt repair and replacement
Upgrades to the latest technology
Less emphasis on:
Our Services:
High-Quality Landscape & Architectural Lighting
Reliable Permanent Lighting Solutions
Call us today and take advantage of our 25% discount (limited time offer)
For more details or to schedule a consultation, visit brightvane-mo.com or call .
*Need to be able to tweak this for future campaigns. Quickly edit verbiage for future marketing campaigns. I.e. a file that can be edited through Canva
*Inspiration photo file (Yard Glow Horizons)
*Would like to incorporate the before and after png
Call: (816) 555-0193
brightvane-mo.com
Updates
I attached a new before and after photo. Please create a design implementing this
Look and feel
Each slider illustrates characteristics of the customer's brand and the style your logo design should communicate.

```html
<!DOCTYPE html>
<html lang="en">
<head>
<meta charset="utf-8">
<title>Brightvane Lighting – Neighborhood Postcard</title>
<link rel="stylesheet" href="https://fonts.googleapis.com/css2?family=Barlow:wght@400;500;600;700&display=swap">
<style>
  :root {
    --page-bg: #e4e4e4;
    --card-bg: #ffffff;
    --gold: #b89a52;
    --ink: #111111;
    --text: #222222;
    --lawn-dark: #1d3015;
    --lawn-mid: #3f5a24;
  }
  * { box-sizing: border-box; margin: 0; padding: 0; }
  html, body { width: 1200px; height: 1200px; overflow: hidden; }
  body {
    background: var(--page-bg);
    font-family: "Barlow", Arial, sans-serif;
    color: var(--text);
  }
  .postcard {
    position: absolute;
    left: 235px; top: 84px;
    width: 730px; height: 1032px;
    background: var(--card-bg);
  }
  .hero-photo {
    position: absolute; left: 0; top: 0;
    width: 730px; height: 451px;
    background:
      radial-gradient(ellipse at 45% 45%, rgba(181,101,44,0.55), transparent 40%),
      linear-gradient(180deg, var(--lawn-dark) 0%, #2b2a20 45%, var(--lawn-mid) 75%, #36501f 100%);
  }
  .brand-name {
    position: absolute; left: 0; top: 478px; width: 100%;
    text-align: center;
    font-size: 34px; font-weight: 600; line-height: 40px;
    color: var(--ink);
  }
  .headline {
    position: absolute; left: 0; top: 552px; width: 100%;
    text-align: center; color: var(--gold);
    font-weight: 600; font-size: 36px; line-height: 44px;
    text-transform: uppercase;
  }
  .intro {
    position: absolute; left: 50px; top: 664px; width: 630px;
    text-align: center; font-size: 14px; line-height: 18px;
  }
  .service-box {
    position: absolute; top: 733px; height: 111px;
    padding: 14px 12px;
    font-size: 14px; line-height: 17px;
  }
  .service-box h2 { font-size: 20px; font-weight: 600; color: var(--ink); margin-bottom: 2px; }
  .service-box ul { list-style: none; }
  .service-box li::before { content: "· "; }
  .services { left: 46px; width: 351px; border: 1.5px solid var(--ink); }
  .maintenance { left: 397px; width: 287px; background: var(--gold); padding-top: 18px; }
  .cta { position: absolute; left: 0; width: 100%; text-align: center; }
  .cta-lead { top: 866px; font-size: 14px; }
  .cta-offer { top: 890px; font-size: 14px; }
  .cta-offer strong { color: var(--gold); font-size: 22px; font-weight: 700; }
  .cta-details { top: 933px; font-size: 14px; }
  .cta-contact { top: 953px; font-size: 21px; font-weight: 700; color: var(--ink); }
  .accent-bar { position: absolute; left: 147px; top: 999px; width: 435px; height: 11px; display: flex; }
  .accent-bar .gold-part { width: 215px; border: 1.5px solid var(--gold); }
  .accent-bar .ink-part { width: 220px; background: var(--ink); }
</style>
</head>
<body>
  <main class="postcard">
    <div class="hero-photo" role="img" aria-label="Brick home at dusk with warm landscape lighting on trees, garden beds and a stone retaining wall over a green lawn"></div>

    <p class="brand-name">Brightvane Lighting</p>

    <h1 class="headline">Elevate your outdoor spaces<br>with premium lighting</h1>

    <p class="intro">Trusted Lighting Design &amp; Maintenance Your neighbor chose us to enhance and maintain their home's beauty and security. Now, we're offering our top-tier services to the entire neighborhood.</p>

    <section class="service-box services">
      <h2>Our Services:</h2>
      <ul>
        <li>High-Quality Landscape &amp; Architectural Lighting</li>
        <li>Reliable Permanent Lighting Solutions</li>
      </ul>
    </section>

    <section class="service-box maintenance">
      <h2>Maintenance Excellence:</h2>
      <ul>
        <li>Regular system check-ups</li>
        <li>Prompt repair and replacement</li>
        <li>Upgrades to the latest technology</li>
      </ul>
    </section>

    <p class="cta cta-lead">Reach out today to schedule your appointment and take advantage of our</p>
    <p class="cta cta-offer"><strong>25% discount</strong> (limited time offer)</p>
    <p class="cta cta-details">For more details or to schedule a consultation, visit brightvane-mo.com or call .</p>
    <p class="cta cta-contact">(816) 555-0193 | brightvane-mo.com</p>

    <div class="accent-bar"><span class="gold-part"></span><span class="ink-part"></span></div>
  </main>
</body>
</html>
```